design a construction company business card

Design business card around our logo. Card must have all the typical info: name, title, address, phone, email, business name, etc. Somewhere on the card I would like to see our motto "Solid in purpose... Driven by dedication." Consider adding a splash of bright orange to the card to complement the blues and silvers/grays in the logo. We are open to metallic inks, textures, etc. We would like to see options on both light and dark backgrounds. The font in the logo is Euro Technic Extended Regular.

```html
<!DOCTYPE html>
<html lang="en">
<head>
<meta charset="utf-8">
<title>Halden Building – Business Card</title>
<link rel="stylesheet" href="https://fonts.googleapis.com/css2?family=Open+Sans:wght@400;600;700&display=swap">
<style>
  :root {
    --backdrop: #2a2a2c;
    --blue-deep: #2c3f9c;
    --blue-mid: #1f5fb8;
    --blue-bright: #1b78c8;
    --blue-text: #2545a8;
    --silver: #9a9a9c;
    --grey-text: #8a8a8c;
    --ink: #3a3a3c;
    --paper: #ffffff;
  }
  * { margin: 0; padding: 0; box-sizing: border-box; }
  html, body { width: 1200px; height: 892px; overflow: hidden; }
  body {
    background: var(--backdrop);
    font-family: "Open Sans", Arial, sans-serif;
    position: relative;
  }
  .card {
    position: absolute;
    width: 600px;
    height: 343px;
    border-radius: 2px;
    box-shadow: 0 12px 30px rgba(0,0,0,0.45);
    overflow: hidden;
  }
  /* Front: tagline side */
  .card-front {
    left: 60px; top: 70px;
    background: radial-gradient(ellipse at 55% 40%, var(--blue-bright) 0%, var(--blue-mid) 40%, var(--blue-deep) 100%);
    color: var(--paper);
    display: flex; flex-direction: column; align-items: center; justify-content: center;
  }
  .front-wordmark {
    display: flex; align-items: center; gap: 12px;
    font-weight: 600; font-size: 38px; letter-spacing: 4px;
  }
  .front-wordmark .mark-square { width: 22px; height: 22px; background: var(--paper); }
  .tagline {
    margin-top: 22px;
    font-size: 15px; letter-spacing: 0.3px;
  }
  /* Back: contact side */
  .card-back {
    left: 540px; top: 480px;
    background: var(--paper);
  }
  .side-band { position: absolute; left: 0; top: 0; width: 130px; height: 100%; }
  .icon { position: absolute; left: 84px; width: 16px; height: 16px; display: block; }
  .icon-person { top: 125px; }
  .icon-pin { top: 186px; }
  .icon-phone { top: 226px; }
  .icon-mail { top: 250px; }
  .icon-web { top: 274px; }
  .wordmark {
    position: absolute; right: 40px; top: 48px;
    display: flex; align-items: center; gap: 10px;
    color: var(--blue-text); font-weight: 700; font-size: 24px; letter-spacing: 2px;
  }
  .wordmark .mark-square { width: 16px; height: 16px; background: var(--blue-text); }
  .contact { position: absolute; left: 160px; top: 120px; }
  .contact .name { color: var(--blue-text); font-weight: 700; font-size: 22px; line-height: 26px; }
  .contact .title { color: var(--grey-text); font-size: 15px; line-height: 20px; letter-spacing: 0.5px; margin-bottom: 16px; }
  .contact .line { color: var(--ink); font-size: 15px; line-height: 20px; }
  .contact .gap { height: 4px; }
</style>
</head>
<body>

<section class="card card-front" aria-label="Card front">
  <div class="front-wordmark"><span class="mark-square"></span>HALDEN</div>
  <p class="tagline">Solid in purpose... Driven by dedication.</p>
</section>

<section class="card card-back" aria-label="Card back">
  <svg class="side-band" viewBox="0 0 130 343" preserveAspectRatio="none" aria-hidden="true">
    <defs>
      <linearGradient id="bandBlue" x1="0" y1="0" x2="0" y2="1">
        <stop offset="0" stop-color="#1b78c8"/>
        <stop offset="1" stop-color="#2c3f9c"/>
      </linearGradient>
    </defs>
    <polygon points="0,0 40,0 120,85 120,110 60,110 0,40" fill="var(--silver)"/>
    <polygon points="0,40 60,110 120,110 120,343 0,343" fill="url(#bandBlue)"/>
    <polygon points="0,0 14,0 14,343 0,343" fill="#2a4aa8"/>
  </svg>

  <svg class="icon icon-person" viewBox="0 0 20 20" aria-hidden="true"><circle cx="10" cy="6" r="4" fill="#fff"/><path d="M2 19c0-5 4-7 8-7s8 2 8 7z" fill="#fff"/></svg>
  <svg class="icon icon-pin" viewBox="0 0 20 20" aria-hidden="true"><path d="M10 1a6 6 0 0 0-6 6c0 5 6 12 6 12s6-7 6-12a6 6 0 0 0-6-6z" fill="#fff"/><circle cx="10" cy="7" r="2.2" fill="#1f5fb8"/></svg>
  <svg class="icon icon-phone" viewBox="0 0 20 20" aria-hidden="true"><path d="M2 8c0-3 4-5 8-5s8 2 8 5l-3 1-1-2H6L5 9z" fill="#fff"/><rect x="4" y="10" width="12" height="8" rx="1" fill="#fff"/></svg>
  <svg class="icon icon-mail" viewBox="0 0 20 20" aria-hidden="true"><rect x="2" y="4" width="16" height="12" fill="#fff"/><path d="M2 4l8 7 8-7" fill="none" stroke="#1f5fb8" stroke-width="1.5"/></svg>
  <svg class="icon icon-web" viewBox="0 0 20 20" aria-hidden="true"><circle cx="10" cy="10" r="8" fill="#fff"/><path d="M2 10h16M10 2c-4 4-4 12 0 16M10 2c4 4 4 12 0 16" fill="none" stroke="#2c3f9c" stroke-width="1.2"/></svg>

  <div class="wordmark"><span class="mark-square"></span>HALDEN BUILDING, INC.</div>

  <div class="contact">
    <p class="name">MARCUS ALDER</p>
    <p class="title">PRESIDENT</p>
    <p class="line">4120 Crestview Lane</p>
    <p class="line">Oak Hollow, NY 10990</p>
    <div class="gap"></div>
    <p class="line">555 0142 7781</p>
    <p class="line">marcus@haldenbuild.com</p>
    <p class="line">www.haldenbuild.com</p>
  </div>
</section>

</body>
</html>
```